Natural Food Packaging - Peanut Butter bars

Name, branding, trade dress for new line of natural/organic peanut based protein bars. The concept its to package a high value natural product for mass consumer consumption.

There will be 2 to 4 flavors initially introduced. Each flavor has a printed film wrapper and shelf display box. The design winner will have first preference for all the packaging work.Think peanut butter chocolate chip, peanut butter with cranberries, coconut, etc.

We are a privately owned, internationally established organic food manufacturer.

This will be a high profile, well recognized project within the industry.

It is an excellent opportunity for a long term business relationship.

Brisco Market(s)

consumers who want a better quality protein bar than they currently buy. Mostly active adults age 18-50

Industry/Entity Type

Business

Requirements
Must have
• A product name/brand and general look and feel. It needs to convey purity, great ingredients/quality, taste and great price.

It needs to have mass appeal...think Brisco and Zipo, not just Verdano Market.
Nice to have
• Package mock up images for 2 or 3 flavors

```html
<!DOCTYPE html>
<html lang="en">
<head>
<meta charset="utf-8">
<title>Moxa Peanut Butter Protein Bar Wrappers</title>
<link rel="stylesheet" href="https://fonts.googleapis.com/css2?family=Jost:wght@700&family=Roboto+Condensed:wght@300;700&family=Libre+Baskerville:wght@400;700&display=swap">
<style>
  :root {
    --page: #f1f1f1;
    --paper: #ffffff;
    --ink: #333333;
    --cran-red: #fc3a4c;
    --cran-teal: #00779a;
    --choc-blue: #0349c4;
    --choc-orange: #ff4c00;
    --choc-yellow: #fda500;
  }
  * { box-sizing: border-box; margin: 0; padding: 0; }
  html, body { width: 1200px; height: 1200px; overflow: hidden; }
  body { background: var(--page); position: relative; font-family: "Roboto Condensed", sans-serif; }

  .wrapper {
    position: absolute; left: 45px; width: 1108px; height: 552px;
    background: var(--paper);
    box-shadow: 0 3px 10px rgba(0,0,0,0.18);
  }
  .wrapper--cranberry { top: 45px; }
  .wrapper--chocolate { top: 618px; }

  .brand-name {
    position: absolute; left: 22px; top: -18px;
    font-family: "Jost", sans-serif; font-weight: 700;
    font-size: 360px; line-height: 1; letter-spacing: -0.05em;
    transform: scaleX(0.88); transform-origin: left top;
    white-space: nowrap;
  }
  .wrapper--cranberry .brand-name { color: var(--cran-teal); }
  .wrapper--chocolate .brand-name { color: var(--choc-orange); }

  .trademark {
    position: absolute; left: 788px; top: 36px;
    font-family: "Roboto Condensed", sans-serif; font-weight: 700;
    font-size: 28px; color: var(--ink);
  }
  .cert-badge { position: absolute; top: 38px; }
  .cert-badge--vegan { left: 928px; }
  .cert-badge--gf { left: 1012px; }

  .descriptor {
    position: absolute; left: 22px; top: 312px;
    font-size: 64px; line-height: 1; letter-spacing: -0.03em;
    white-space: nowrap;
  }
  .descriptor b { font-weight: 700; }
  .descriptor .light { font-weight: 300; }

  .claims {
    position: absolute; right: 10px; top: 188px;
    list-style: none; text-align: right;
    font-family: "Libre Baskerville", serif; font-weight: 400;
    font-size: 31px; line-height: 37px; letter-spacing: -0.03em;
  }

  .flavor-band {
    position: absolute; left: 0; bottom: 0; width: 100%; height: 168px;
  }
  .wrapper--cranberry .flavor-band { background: var(--cran-red); }
  .wrapper--chocolate .flavor-band { background: var(--choc-yellow); }

  .flavor-name {
    position: absolute; left: 24px; top: 28px;
    font-family: "Libre Baskerville", serif; font-weight: 700;
    font-size: 74px; line-height: 1.2; color: var(--paper);
    letter-spacing: 0.01em; white-space: nowrap;
  }
  .net-weight {
    position: absolute; right: 16px; top: 66px;
    font-family: "Libre Baskerville", serif; font-weight: 700;
    font-size: 26px; color: var(--ink); letter-spacing: -0.02em;
  }
  .fineprint {
    position: absolute; left: 28px; bottom: 5px;
    font-size: 18.5px; color: var(--ink); letter-spacing: -0.01em;
    white-space: nowrap;
  }

  .c-red { color: var(--cran-red); }
  .c-teal { color: var(--cran-teal); }
  .c-ink { color: var(--ink); }
  .c-blue { color: var(--choc-blue); }
  .c-orange { color: var(--choc-orange); }
  .c-yellow { color: var(--choc-yellow); }
</style>
</head>
<body>

<section class="wrapper wrapper--cranberry">
  <div class="brand-name">Moxa</div>
  <div class="trademark">TM</div>
  <svg class="cert-badge cert-badge--vegan" width="52" height="52" viewBox="0 0 52 52" role="img" aria-label="Vegan certification badge"><circle cx="26" cy="26" r="23" fill="none" stroke="#222" stroke-width="3"/></svg>
  <svg class="cert-badge cert-badge--gf" width="54" height="54" viewBox="0 0 54 54" role="img" aria-label="Gluten-free certification badge"><circle cx="27" cy="27" r="22" fill="none" stroke="#222" stroke-width="4"/></svg>
  <div class="descriptor"><b class="c-red">Peanut</b> <b class="c-teal">Butter</b> <b class="c-ink">Protein</b> <span class="light c-ink">bar</span></div>
  <ul class="claims">
    <li class="c-teal">Gluten-free.</li>
    <li class="c-ink">All natural.</li>
    <li class="c-red">Omega-3 from flax.</li>
    <li class="c-teal">12 grams of protein.</li>
    <li class="c-ink">Good source of fiber.</li>
  </ul>
  <div class="flavor-band">
    <div class="flavor-name">{Peanut &amp; Cranberry}</div>
    <div class="net-weight">net wt 2.05 oz</div>
    <p class="fineprint">A product of Such&amp;Such Co. Pty Ltd 2013. All rights reserved. 123 Street Name, Postcode, Country. Generic fineprint.</p>
  </div>
</section>

<section class="wrapper wrapper--chocolate">
  <div class="brand-name">Moxa</div>
  <div class="trademark">TM</div>
  <svg class="cert-badge cert-badge--vegan" width="52" height="52" viewBox="0 0 52 52" role="img" aria-label="Vegan certification badge"><circle cx="26" cy="26" r="23" fill="none" stroke="#222" stroke-width="3"/></svg>
  <svg class="cert-badge cert-badge--gf" width="54" height="54" viewBox="0 0 54 54" role="img" aria-label="Gluten-free certification badge"><circle cx="27" cy="27" r="22" fill="none" stroke="#222" stroke-width="4"/></svg>
  <div class="descriptor"><b class="c-blue">Peanut</b> <b class="c-orange">Butter</b> <b class="c-yellow">Protein</b> <span class="light c-yellow">bar</span></div>
  <ul class="claims">
    <li class="c-blue">Gluten-free.</li>
    <li class="c-yellow">All natural.</li>
    <li class="c-orange">Omega-3 from flax.</li>
    <li class="c-blue">12 grams of protein.</li>
    <li class="c-yellow">Good source of fiber.</li>
  </ul>
  <div class="flavor-band">
    <div class="flavor-name">{Peanut &amp; Chocolate}</div>
    <div class="net-weight">net wt 2.05 oz</div>
    <p class="fineprint">A product of Such&amp;Such Co. Pty Ltd 2013. All rights reserved. 123 Street Name, Postcode, Country. Generic fineprint.</p>
  </div>
</section>

</body>
</html>
```